Colour consulting and Interior design company needs a squarespace web design

we need a website design for squarespace for a Melbourne based company called 'Brightwell Rooms' which incorporates the existing logo. The company primarily provides colour consulting for residential and commercial as well as interior design services. Schemes are personalised for each client. I would like the design to have some colour and use the colour palette provided but it is not is not totally exclusive. The final design should indicate character, playfulness, functionality , harmony and joy. I like the blue/green core colour with the white and would like that to be incorporated.
as per image provided below - double sided
4 page
- space for some images but not too many.
- Page for booking consultation
- real images of houses

```html
<!DOCTYPE html>
<html lang="en">
<head>
<meta charset="utf-8">
<title>Brightwell Rooms — Colour Consulting &amp; Interior Design</title>
<link rel="stylesheet" href="https://fonts.googleapis.com/css2?family=Work+Sans:wght@400;500;600&display=swap">
<style>
:root{
  --teal:#2a8c98;
  --teal-dark:#16707e;
  --heading:#1b6f80;
  --ink:#333a3d;
  --muted:#6a7073;
  --white:#ffffff;
  --footer:#e6e7e8;
}
*{margin:0;padding:0;box-sizing:border-box}
html,body{width:1200px;height:3557px;overflow:hidden}
body{position:relative;background:var(--white);font-family:"Work Sans",Arial,sans-serif;color:var(--ink)}
.abs{position:absolute}
.img{position:absolute}
.caps{text-transform:uppercase;letter-spacing:.18em}
.btn{position:absolute;display:flex;align-items:center;justify-content:center;background:var(--teal-dark);color:var(--white);font-size:11px;letter-spacing:.2em;text-transform:uppercase;font-weight:500}

/* header */
.header{position:absolute;left:0;top:0;width:1200px;height:78px;background:var(--white)}
.brand{position:absolute;display:flex;align-items:center;gap:8px;font-weight:600;color:var(--heading);font-size:20px;white-space:nowrap}
.brand-mark{width:26px;height:26px;background:var(--heading)}
.contact-line{position:absolute;top:16px;font-size:10px;color:var(--muted);display:flex;align-items:center;gap:6px}
.nav{position:absolute;top:50px;left:410px;display:flex;align-items:center;font-size:10px;letter-spacing:.18em;text-transform:uppercase;color:var(--ink)}
.nav a{color:inherit;text-decoration:none}
.callback{position:absolute;left:797px;top:47px;width:168px;height:24px;background:var(--teal-dark);color:var(--white);font-size:10px;letter-spacing:.16em;display:flex;align-items:center;justify-content:center;text-transform:uppercase}

/* hero */
.hero{position:absolute;left:0;top:78px;width:1200px;height:373px;background:radial-gradient(ellipse at 60% 50%,#35a0ab,#257f8c 75%)}
.hero-kicker{left:235px;top:90px;color:var(--white);font-size:12px}
.hero-title{left:233px;top:112px;color:var(--white);font-size:31px;font-weight:400;letter-spacing:.16em;line-height:40px}
.hero-btn{left:235px;top:209px;width:155px;height:29px;background:var(--white);color:var(--teal-dark)}
.dots{position:absolute;left:512px;top:349px;display:flex;gap:4px}
.dots span{width:52px;height:3px;background:rgba(255,255,255,.85)}

/* service panels */
.panel-label{font-size:10px;color:var(--ink)}
.panel-title{font-size:17px;letter-spacing:.22em;line-height:36px;color:var(--ink);text-transform:uppercase}

/* trusted */
.section-title{color:var(--heading);font-size:17px;font-weight:600;letter-spacing:.12em;text-transform:uppercase;text-align:center;width:1200px;left:0}
.lead{font-size:10px;line-height:20px;color:var(--muted);text-align:center;letter-spacing:.04em}
.tile-caption{font-size:9px;letter-spacing:.22em;text-transform:uppercase}
.tile-caption b{display:block;color:var(--heading);font-weight:600}
.tile-caption span{color:var(--muted)}

/* features */
.feature-title{color:var(--heading);font-size:12px;font-weight:600;letter-spacing:.16em;text-transform:uppercase}
.feature-copy{font-size:9px;line-height:19px;color:var(--muted);letter-spacing:.03em;width:230px}

/* blog */
.post-title{font-size:11px;letter-spacing:.2em;text-transform:uppercase;color:var(--ink)}
.post-more{font-size:8px;letter-spacing:.2em;text-transform:uppercase;color:var(--ink);font-weight:600}

/* footer */
.footer{position:absolute;left:0;top:3333px;width:1200px;height:224px;background:var(--footer)}
.foot-head{font-size:9px;letter-spacing:.2em;text-transform:uppercase;font-weight:600;color:var(--ink)}
.foot-text{font-size:9px;line-height:18px;color:var(--ink)}
.social{width:20px;height:20px;position:absolute}
</style>
</head>
<body>

<header class="header">
  <div class="brand" style="left:235px;top:22px"><span class="brand-mark"></span>Brightwell Rooms</div>
  <div class="contact-line" style="left:682px">
    <svg width="12" height="12" viewBox="0 0 12 12"><path d="M3 1l2 2-1 2c1 1.5 2 2.5 3 3l2-1 2 2-1 2C5 11 1 7 1 2z" fill="var(--teal)"/></svg>0400 118 260
  </div>
  <div class="contact-line" style="left:786px">
    <svg width="13" height="10" viewBox="0 0 13 10"><rect x=".5" y=".5" width="12" height="9" fill="none" stroke="var(--teal)"/><path d="M.5 .5l6 5 6-5" fill="none" stroke="var(--teal)"/></svg>studio@brightwellrooms.example
  </div>
  <nav class="nav">
    <svg width="12" height="11" viewBox="0 0 12 11" style="margin-right:30px"><path d="M6 0l6 5h-2v6H7V7H5v4H2V5H0z" fill="var(--teal-dark)"/></svg>
    <a style="margin-right:40px">About</a>
    <a style="margin-right:40px">Products &#709;</a>
    <a style="margin-right:40px">Blog</a>
    <a>Contact</a>
  </nav>
  <div class="callback">Request a callback</div>
</header>

<section class="hero">
  <div class="abs caps hero-kicker">Websites</div>
  <h1 class="abs hero-title">THE LEADER IN<br>WEBSITE DESIGN</h1>
  <div class="btn hero-btn">Get a quote</div>
  <div class="img" role="img" aria-label="Illustration of an open-plan office with desks and bookshelves" style="left:570px;top:16px;width:450px;height:340px;background:linear-gradient(160deg,#e9eef0 0%,#b9c9cc 50%,#5b6b70 100%);clip-path:polygon(30% 0,100% 10%,100% 75%,60% 100%,0 70%,0 30%);opacity:.9"></div>
  <div class="dots"><span></span><span></span><span></span></div>
</section>

<section>
  <div class="img" role="img" aria-label="Illustration of a bright commercial workspace" style="left:0;top:453px;width:598px;height:202px;background:linear-gradient(90deg,#eeeeec 0%,#e4e2dd 55%,#cfc9bf 100%)"></div>
  <div class="abs caps panel-label" style="left:220px;top:492px">Colour consulting</div>
  <div class="abs panel-title" style="left:220px;top:508px">Commercial<br>Design</div>
  <div class="img" role="img" aria-label="Illustration of a residential living room with staircase" style="left:598px;top:453px;width:602px;height:202px;background:linear-gradient(90deg,#d9d2c5 0%,#c8b59a 60%,#8b6b48 100%)"></div>
  <div class="abs caps panel-label" style="left:647px;top:492px">Colour consulting</div>
  <div class="abs panel-title" style="left:647px;top:508px">Residential<br>Design</div>
</section>

<section>
  <h2 class="abs section-title" style="top:698px">Trusted by the world's best</h2>
  <p class="abs lead" style="left:300px;top:740px;width:600px">Lorem Ipsum is simply dummy text of the printing and typesetting industry. Lorem Ipsum has been the industry's standard dummy text ever since the 1500s, when an unknown printer took a galley of type and scrambled it to make a type specimen book.</p>
  <div class="btn" style="left:517px;top:825px;width:166px;height:48px">See all stories</div>

  <div class="img" role="img" aria-label="Illustration of a green kitchen interior" style="left:0;top:923px;width:221px;height:251px;background:linear-gradient(180deg,#cfdcc3,#8ea47c 55%,#6c7160)"></div>
  <div class="img" role="img" aria-label="Illustration of an orange lounge with sofa and plant" style="left:242px;top:923px;width:225px;height:251px;background:linear-gradient(160deg,#f39a1f,#e05a1a 70%,#b8860b)"></div>
  <div class="img" role="img" aria-label="Illustration of a blue bedroom with doorway" style="left:489px;top:923px;width:225px;height:251px;background:linear-gradient(90deg,#3d5f8c 0%,#c9d8e6 45%,#eef2f5 100%)"></div>
  <div class="img" role="img" aria-label="Illustration of a patterned sitting room with armchairs" style="left:735px;top:923px;width:226px;height:251px;background:linear-gradient(180deg,#b5793a,#e3b36a 55%,#f2d79a)"></div>
  <div class="img" role="img" aria-label="Illustration of a warm bedroom with wooden headboard" style="left:982px;top:923px;width:218px;height:251px;background:linear-gradient(180deg,#e0c8a8,#c99a6b 55%,#6e4a36)"></div>

  <div class="abs tile-caption" style="left:0;top:1186px"><b>Lorem ipsum</b><span>Dummy text of typesetting</span></div>
  <div class="abs tile-caption" style="left:242px;top:1186px"><b>Lorem ipsum</b><span>Dummy text of typesetting</span></div>
  <div class="abs tile-caption" style="left:489px;top:1186px"><b>Lorem ipsum</b><span>Dummy text of typesetting</span></div>
  <div class="abs tile-caption" style="left:735px;top:1186px"><b>Lorem ipsum</b><span>Dummy text of typesetting</span></div>
  <div class="abs tile-caption" style="left:982px;top:1186px"><b>Lorem ipsum</b><span>Text of the typesetting</span></div>
</section>

<section>
  <div class="img" role="img" aria-label="Illustration of a kitchen shelf interior" style="left:235px;top:1319px;width:220px;height:270px;background:linear-gradient(180deg,#ece6dd,#d8c2a0 60%,#b08e64)"></div>
  <div class="img" role="img" aria-label="Illustration of a home office with desk and chair" style="left:378px;top:1420px;width:293px;height:212px;background:linear-gradient(180deg,#d6a56a,#c88f52 55%,#5b3a28)"></div>
  <div class="abs feature-title" style="left:735px;top:1318px">Lorem ipsum is simply</div>
  <p class="abs feature-copy" style="left:735px;top:1346px">Lorem Ipsum is simply dummy text of the printing and typesetting industry. Lorem Ipsum has been the industry's standard dummy text ever since the 1500s, when an unknown printer took a galley of type and scrambled it to make a type specimen book. It has survived not only five centuries, but also the leap into electronic typesetting, remaining essentially unchanged.</p>
  <div class="btn" style="left:735px;top:1542px;width:166px;height:47px">See all stories</div>
</section>

<section>
  <div class="img" role="img" aria-label="Illustration of a dim living room with sofa and television" style="left:0;top:1687px;width:1200px;height:322px;background:linear-gradient(180deg,#5e5f61 0%,#565759 60%,#48494b 100%)"></div>
  <div class="abs caps" style="left:0;width:1200px;top:1788px;text-align:center;color:var(--white);font-size:27px;letter-spacing:.1em">Lorem ipsum is simply text</div>
  <div class="btn" style="left:517px;top:1848px;width:166px;height:45px">Know more</div>
</section>

<section>
  <h2 class="abs section-title" style="top:2058px;font-size:13px">Our blog</h2>
  <div class="img" role="img" aria-label="Illustration of a lounge with red chair" style="left:278px;top:2109px;width:206px;height:163px;background:linear-gradient(180deg,#efece2,#c9c98a 60%,#b5b336)"></div>
  <div class="img" role="img" aria-label="Illustration of a room with a framed feature" style="left:496px;top:2109px;width:208px;height:163px;background:linear-gradient(180deg,#f3ede6,#e7d7c6)"></div>
  <div class="abs" style="left:496px;top:2109px;width:208px;height:163px;border:6px solid #f0d9c4"></div>
  <div class="abs" style="left:587px;top:2148px;width:26px;height:26px;background:var(--teal-dark);color:var(--white);display:flex;align-items:center;justify-content:center;font-size:16px">+</div>
  <div class="abs" style="left:496px;top:2184px;width:208px;text-align:center;font-size:8px;letter-spacing:.12em;color:var(--ink);line-height:14px">Lorem ipsum is simply<br><span class="caps" style="font-size:7px">Lorem ipsum<br>is simply</span></div>
  <div class="img" role="img" aria-label="Illustration of a white office with black chair" style="left:716px;top:2109px;width:207px;height:163px;background:linear-gradient(180deg,#f2f2f2,#dcdcdc 60%,#bfbfbf)"></div>

  <div class="abs post-title" style="left:278px;top:2290px">Lorem ipsum is simply</div>
  <div class="abs post-title" style="left:496px;top:2290px">Lorem ipsum is simply</div>
  <div class="abs post-title" style="left:716px;top:2290px">Lorem ipsum is simply</div>
  <div class="abs post-more" style="left:278px;top:2313px">More</div>
  <div class="abs post-more" style="left:496px;top:2313px">More</div>
  <div class="abs post-more" style="left:716px;top:2313px">More</div>

  <div class="img" role="img" aria-label="Illustration of a green-walled bedroom" style="left:278px;top:2363px;width:206px;height:161px;background:linear-gradient(180deg,#c7d99a,#b5c884 55%,#6b7748)"></div>
  <div class="img" role="img" aria-label="Illustration of an olive living room with grey sofa" style="left:496px;top:2363px;width:208px;height:161px;background:linear-gradient(180deg,#9cb04a,#8fa03f 60%,#6b5a3f)"></div>
  <div class="img" role="img" aria-label="Illustration of a study with window and shelves" style="left:716px;top:2363px;width:207px;height:161px;background:linear-gradient(180deg,#c5d1a8,#a9bf8c 60%,#7f6c52)"></div>

  <div class="abs post-title" style="left:278px;top:2544px">Lorem ipsum is simply</div>
  <div class="abs post-title" style="left:496px;top:2544px">Lorem ipsum is simply</div>
  <div class="abs post-title" style="left:716px;top:2544px">Lorem ipsum is simply</div>
  <div class="abs post-more" style="left:278px;top:2566px">More</div>
  <div class="abs post-more" style="left:496px;top:2566px">More</div>
  <div class="abs post-more" style="left:716px;top:2566px">More</div>

  <div class="btn" style="left:517px;top:2621px;width:166px;height:48px">View all blog</div>
</section>

<section>
  <div class="img" role="img" aria-label="Illustration of a desk with laptop and red chair" style="left:0;top:2718px;width:1200px;height:200px;background:linear-gradient(180deg,#636465 0%,#555657 55%,#4a4340 100%)"></div>
  <div class="abs caps" style="left:230px;width:207px;top:2800px;text-align:right;color:var(--white);font-size:15px;font-weight:600;line-height:19px;letter-spacing:.16em">Brightwell<br>Rooms</div>
  <div class="abs caps" style="left:453px;top:2802px;width:260px;color:#dcdcdc;font-size:8px;line-height:14px">Lorem ipsum is simply dummy text of the printing and</div>
  <div class="abs caps" style="left:759px;top:2807px;width:81px;height:19px;border:1px solid var(--white);color:var(--white);font-size:8px;display:flex;align-items:center;justify-content:center">Locate us</div>
</section>

<section>
  <div class="img" role="img" aria-label="Illustration of a white brick wall with pendant lamps" style="left:235px;top:2967px;width:220px;height:270px;background:linear-gradient(180deg,#eeeeee,#dedede 60%,#c7c2bb)"></div>
  <div class="img" role="img" aria-label="Illustration of a colourful lounge with lamp and clock" style="left:378px;top:3071px;width:293px;height:214px;background:linear-gradient(135deg,#f2c94c 0%,#f08a3c 50%,#d9622b 100%)"></div>
  <div class="abs feature-title" style="left:735px;top:3010px">Lorem ipsum is simply</div>
  <p class="abs feature-copy" style="left:735px;top:3038px">Lorem Ipsum is simply dummy text of the printing and typesetting industry. Lorem Ipsum has been the industry's standard dummy text ever since the 1500s.</p>
  <div class="btn" style="left:735px;top:3148px;width:166px;height:47px">View all</div>
  <div class="abs" style="left:972px;top:3314px;width:31px;height:31px;background:#111">
    <svg width="31" height="31" viewBox="0 0 31 31"><path d="M11 18l4.5-5 4.5 5" fill="none" stroke="#fff" stroke-width="2"/></svg>
  </div>
</section>

<footer class="footer">
  <div class="brand" style="left:235px;top:57px;font-size:15px;gap:7px"><span class="brand-mark" style="width:20px;height:20px"></span>Brightwell Rooms</div>
  <div class="abs foot-text" style="left:235px;top:96px;font-size:7px;line-height:11px">© 2016 www.brightwellrooms.example<br>All Rights Reserved</div>

  <div class="abs foot-head" style="left:420px;top:57px">Address</div>
  <div class="abs foot-text" style="left:420px;top:74px">Elmhurst VIC 3172<br>Australia</div>
  <div class="abs foot-text" style="left:420px;top:114px;display:flex;align-items:center;gap:6px"><svg width="11" height="11" viewBox="0 0 12 12"><path d="M3 1l2 2-1 2c1 1.5 2 2.5 3 3l2-1 2 2-1 2C5 11 1 7 1 2z" fill="var(--teal)"/></svg>Tel: 0400 118 260</div>
  <div class="abs foot-text" style="left:420px;top:132px;display:flex;align-items:center;gap:6px"><svg width="12" height="9" viewBox="0 0 13 10"><rect x=".5" y=".5" width="12" height="9" fill="none" stroke="var(--teal)"/><path d="M.5 .5l6 5 6-5" fill="none" stroke="var(--teal)"/></svg>studio@brightwellrooms.example</div>

  <div class="abs foot-head" style="left:652px;top:57px">Sitemap</div>
  <div class="abs foot-text" style="left:652px;top:74px">Home<br>About<br>Products<br>Blog<br>Contact</div>

  <div class="abs foot-head" style="left:735px;top:57px">Products</div>
  <div class="abs foot-text" style="left:735px;top:74px;width:100px">Lorem ipsum is simply dummy text of the printing typesetting industry Lorem ipsum</div>

  <div class="abs foot-head" style="left:861px;top:57px">Follow us</div>
  <div class="social" style="left:861px;top:80px;background:#3b5998"></div>
  <div class="social" style="left:891px;top:80px;background:#1da1f2"></div>
  <div class="social" style="left:921px;top:80px;background:#0e76a8"></div>
  <div class="social" style="left:861px;top:110px;background:#1da1f2"></div>
  <div class="social" style="left:891px;top:110px;background:#d83a3a"></div>
  <div class="social" style="left:921px;top:110px;background:#8a8a8a"></div>

  <div class="abs caps" style="left:700px;width:268px;top:186px;text-align:right;font-size:7px;color:var(--ink)">Privacy | Legal | T&amp;C | Cookies</div>
</footer>

</body>
</html>
```